UK Glass Restoration Company needs a Direct Mail Postcard Design

We need a HARD HITTING, COMPELLING 300dpi Camera Ready double sided postcard.
The dimensions will be 109mm x 152mm including bleed. We are a scratched glass repair / etched graffiti removal glass restoration company based in London, UK.
We operate mainly within the construction and commercial marketplace, however this particular postcard design is aimed solely at shop owners who have become victims of vandalism, due to etched graffiti tags and or scratches being left on their shop front glass.
We wish to focus the shop / business owners mind to the negative impact such vandalism has on the image of their business and how we are able to offer a quick and cost effective solution
We will supply text for both sides of the postcard along with relevant images, company logo and previous flyer designs, however we are happy for the selected designer to source suitable alternative images provided they are in keeping with the exact "Before" and "After" theme.
The finished postcard must preferably have a white background, but again we are open to creative suggestions.
Target Market(s)
UK SHOP OWNERS
Industry/Entity Type
It Company

```html
<!DOCTYPE html>
<html lang="en">
<head>
<meta charset="utf-8">
<title>Lucent Glass Repairs – Postcard Proof</title>
<link rel="stylesheet" href="https://fonts.googleapis.com/css2?family=Saira+Condensed:wght@500;600;700&family=Roboto+Condensed:wght@400;500;700&display=swap">
<style>
  :root{
    --paper:#ffffff;
    --ink:#1a1a1a;
    --night:#0d1420;
    --night-line:#1d2a3a;
    --glass-1:#7d8ca6;
    --glass-2:#a9b4c6;
    --glass-3:#5d6d88;
    --yellow:#f2ea1a;
    --orange:#d35a10;
    --orange-hi:#ef6f16;
    --orange-deep:#b9490a;
    --logo-blue:#1c9ad6;
    --coupon-grey:#e4e4e4;
    --stamp-red:#d8262a;
    --white:#ffffff;
  }
  *{box-sizing:border-box;margin:0;padding:0}
  html,body{width:1200px;height:780px;overflow:hidden;background:var(--paper)}
  body{position:relative;font-family:"Roboto Condensed",Arial,sans-serif;color:var(--ink)}

  .crop-marks{position:absolute;inset:0;pointer-events:none}
  .side-label{position:absolute;top:18px;font-family:"Saira Condensed",sans-serif;font-weight:600;font-size:17px;letter-spacing:.5px;transform:translateX(-50%)}

  .card{position:absolute;top:46px;width:502px;height:687px;overflow:hidden}
  .card--front{left:62px;background:var(--night)}
  .card--back{left:636px;background:linear-gradient(180deg,var(--orange-hi),var(--orange) 60%,var(--orange-deep))}

  /* brand block */
  .brand{position:absolute;background:var(--white);display:flex;align-items:center;justify-content:center;gap:6px;box-shadow:4px 4px 0 #111}
  .brand__dot{width:10px;height:10px;border-radius:50%;background:var(--logo-blue)}
  .brand__name{font-family:"Roboto Condensed",sans-serif;font-weight:400;font-size:32px;color:var(--logo-blue);letter-spacing:.5px}

  /* front */
  .front__band-top{position:absolute;left:0;top:0;width:100%;height:80px;background:repeating-linear-gradient(90deg,var(--night) 0 3px,var(--night-line) 3px 5px)}
  .front__photo{position:absolute;left:0;top:80px;width:100%;height:486px;background:linear-gradient(180deg,var(--glass-2) 0%,var(--glass-1) 30%,var(--glass-3) 70%,var(--glass-1) 100%)}
  .front__band-bottom{position:absolute;left:0;top:566px;width:100%;height:121px;background:repeating-linear-gradient(90deg,var(--night) 0 3px,var(--night-line) 3px 5px)}
  .front__brand{left:304px;top:40px;width:148px;height:62px}
  .front__headline{position:absolute;left:0;top:0;font-family:"Saira Condensed",sans-serif;font-weight:700;color:var(--white);text-transform:uppercase;line-height:1;text-shadow:0 2px 4px rgba(0,0,0,.35)}
  .front__headline span{position:absolute;white-space:nowrap}
  .hl-before{left:82px;top:102px;font-size:44px;color:#e8ecf2}
  .hl-repair{left:103px;top:138px;font-size:80px}
  .hl-bad{left:82px;top:218px;font-size:46px}
  .hl-first{left:110px;top:257px;font-size:46px}
  .hl-impression{left:44px;top:291px;font-size:58px}
  .front__subhead{position:absolute;left:44px;top:372px;font-family:"Saira Condensed",sans-serif;font-weight:600;font-size:26px;line-height:1.1;color:var(--yellow);white-space:nowrap}
  .front__body{position:absolute;left:44px;top:408px;width:434px;font-size:11.5px;font-weight:500;line-height:14px;color:var(--white);text-align:justify}
  .front__rule{position:absolute;left:44px;top:533px;width:434px;border-top:1px dashed rgba(255,255,255,.75)}
  .front__cta{position:absolute;left:44px;top:549px;font-family:"Saira Condensed",sans-serif;font-weight:600;font-size:19px;line-height:1;color:var(--yellow)}
  .front__phone{position:absolute;left:44px;top:570px;font-family:"Saira Condensed",sans-serif;font-weight:500;font-size:22px;line-height:1;color:var(--white)}
  .front__web{position:absolute;left:44px;top:593px;font-size:15px;line-height:1;color:var(--white)}

  /* back */
  .back__kicker{position:absolute;left:42px;top:36px;font-family:"Saira Condensed",sans-serif;font-weight:600;font-size:26px;color:var(--white);line-height:1}
  .back__title{position:absolute;left:72px;top:58px;font-family:"Saira Condensed",sans-serif;font-weight:700;font-size:37px;color:var(--white);line-height:1}
  .back__brand{left:312px;top:66px;width:146px;height:60px;box-shadow:3px 3px 0 rgba(0,0,0,.35)}
  .back__photo{position:absolute;left:0;top:106px;width:100%;height:290px;background:linear-gradient(100deg,#2f6a78 0%,#4fb7c8 35%,#8fd3dd 55%,#6c8fb0 75%,#4a7fb8 100%)}
  .back__why{position:absolute;left:24px;top:416px;font-family:"Saira Condensed",sans-serif;font-weight:600;font-size:19px;line-height:1;color:var(--yellow)}
  .back__list{position:absolute;left:24px;top:443px;width:458px;list-style:none;font-size:11px;line-height:13.6px;color:var(--white)}
  .back__list li{position:relative;padding-left:17px;text-align:justify}
  .back__list li::before{content:"•";position:absolute;left:0}
  .coupon{position:absolute;left:0;top:578px;width:100%;height:47px;background:var(--coupon-grey);border-top:1.5px dashed #333;border-bottom:1.5px dashed #333}
  .coupon__label{position:absolute;left:24px;top:6px;font-family:"Saira Condensed",sans-serif;font-weight:600;font-size:17px;line-height:1;color:#c3281d}
  .coupon__offer{position:absolute;left:24px;top:24px;font-size:12px;line-height:1.2;color:#111;white-space:nowrap}
  .coupon__offer strong{font-size:16px}
  .coupon__stamp{position:absolute;left:234px;top:-16px;width:122px;padding:3px 4px;background:var(--stamp-red);border:2px solid var(--white);color:var(--white);font-family:"Roboto Condensed",sans-serif;font-weight:700;font-size:8.5px;line-height:10px;text-align:center;transform:rotate(-7deg);box-shadow:1px 1px 3px rgba(0,0,0,.4)}
  .coupon__scissors{position:absolute;right:46px;top:-10px}
  .back__footer{position:absolute;left:24px;top:640px;font-family:"Saira Condensed",sans-serif;font-weight:600;font-size:15px;line-height:1.1;color:var(--yellow);white-space:nowrap}
  .back__footer .contact{color:var(--white);font-family:"Roboto Condensed",sans-serif;font-weight:400}
  .back__footer .contact b{font-weight:700}
</style>
</head>
<body>

<svg class="crop-marks" width="1200" height="780" aria-hidden="true">
  <g stroke="#111" stroke-width="1">
    <line x1="80" y1="30" x2="80" y2="46"/><line x1="546" y1="30" x2="546" y2="46"/>
    <line x1="80" y1="733" x2="80" y2="749"/><line x1="546" y1="733" x2="546" y2="749"/>
    <line x1="46" y1="64" x2="62" y2="64"/><line x1="46" y1="715" x2="62" y2="715"/>
    <line x1="564" y1="64" x2="580" y2="64"/><line x1="564" y1="715" x2="580" y2="715"/>
    <line x1="654" y1="30" x2="654" y2="46"/><line x1="1120" y1="30" x2="1120" y2="46"/>
    <line x1="654" y1="733" x2="654" y2="749"/><line x1="1120" y1="733" x2="1120" y2="749"/>
    <line x1="620" y1="64" x2="636" y2="64"/><line x1="620" y1="715" x2="636" y2="715"/>
    <line x1="1138" y1="64" x2="1154" y2="64"/><line x1="1138" y1="715" x2="1154" y2="715"/>
  </g>
</svg>

<div class="side-label" style="left:313px">FRONT</div>
<div class="side-label" style="left:887px">BACK</div>

<section class="card card--front">
  <div class="front__band-top"></div>
  <div class="front__photo" role="img" aria-label="Close-up photo of a shop window covered in scratches and etched graffiti"></div>
  <div class="front__band-bottom"></div>

  <div class="brand front__brand"><span class="brand__dot"></span><span class="brand__name">Lucent</span></div>

  <h1 class="front__headline">
    <span class="hl-before">Before</span>
    <span class="hl-repair">Repair –</span>
    <span class="hl-bad">A Bad</span>
    <span class="hl-first">First</span>
    <span class="hl-impression">Impression</span>
  </h1>

  <h2 class="front__subhead">Don't Let Vandals Wreck Your Image!</h2>
  <p class="front__body">What's on display in your shop window? If it's graffiti, vandalism, or just wear and tear, that's the first impression your customers get – and it's not good. Lucent Glass Repairs remove damage from glass windows, making them sparkling clear – without replacing the glass! Our glass repair work is effective, green, and very economical. See our coupon on the other side to save even more!</p>

  <div class="front__rule"></div>
  <p class="front__cta">Call Now For Expert Advice :</p>
  <p class="front__phone">0800 555 0142</p>
  <p class="front__web">www.lucentglassrepairs.co.uk</p>
</section>

<section class="card card--back">
  <p class="back__kicker">AFTER REPAIR –</p>
  <h1 class="back__title">CLEAR AS NEW!</h1>
  <div class="back__photo" role="img" aria-label="Photo of a restored curved glass wall in a bright office reception"></div>
  <div class="brand back__brand"><span class="brand__dot"></span><span class="brand__name">Lucent</span></div>

  <h2 class="back__why">Why Lucent Glass Repairs?</h2>
  <ul class="back__list">
    <li>We repair most shop window glass! We repair laminated, tempered, toughened, mirrored, tinted, and even ballistic glass.</li>
    <li>We repair curved glass! Don't replace expensive curved panes - get the like-new look for less by repairing.</li>
    <li>Finer work! We remove etched graffiti tags, scratches, mineral deposits, and acid etched graffiti damage.</li>
    <li>Edge expertise! We can repair even deep scratches as close as 20mm from the edge of the glass.</li>
    <li>Save time and money! Typical savings of up to 80% over the cost of glass replacement, with zero downtime during repair.</li>
  </ul>

  <div class="coupon">
    <p class="coupon__label">COUPON BORDER</p>
    <p class="coupon__offer"><strong>Save 20%</strong> off our regular prices for scratch repair, restoration, and etched graffiti removal.</p>
    <div class="coupon__stamp">ACT NOW – OFFER EXPIRES<br>DATE : XXXXXXX</div>
    <svg class="coupon__scissors" width="26" height="20" viewBox="0 0 30 22" aria-hidden="true">
      <g fill="none" stroke="#111" stroke-width="2">
        <circle cx="6" cy="5" r="4"/><circle cx="6" cy="17" r="4"/>
        <line x1="9" y1="7" x2="28" y2="17"/><line x1="9" y1="15" x2="28" y2="5"/>
      </g>
    </svg>
  </div>

  <p class="back__footer">Call Now For Expert Advice : <span class="contact"><b>0800 555 0142</b>, www.lucentglassrepairs.co.uk.</span></p>
</section>

</body>
</html>
```